Re-design of current business cards

We are updating our website with new colors and layout. Would like to re-design our business cards to co-ordinate. See attached pdf with new Brindlecraft website colors. We would also like to combine our 2 brands on the one business card. Attached is the new design for our Brindlecraft website, current business cards, which are one sided, brindlecraft logo in tiff, .ai for fonts. Brindlecraft logo font is Optimum, Quillmarsh website home page image, Quillmarsh brand statics for products which includes the logo for this brand.

Quillmarsh brand will stay the dark gray on the website. See attached statics for product and website home page.
Updates

The business cards will be 2 sided. Brindlecraft Brand on one side and Quillmarsh Brand on the other. The colors for Brindlecraft need to follow the color scheme of the brindlecraft website pdf I uploaded. The colors are a blue, lighter teal blue and white. Quillmarsh needs to follow the dark gray color on files uploaded

Target Market(s)

The trade and consumers

Industry/Entity Type

Home Furnishing

Contact Information for Business Card

We are updating our website with new colors and layout. Would like to re-design our business cards to co-ordinate. We would also like to combine our 2 brands onto 1 2 sided business cards.

Requirements
Must have
• Colors that match our new website, see attached image.
• RGB colors
• navy -#152842
• teal - 98aeb9
• The gray color used for Quillmarsh brands.
• ll logos and fonts should stay the same.

```html
<!DOCTYPE html>
<html lang="en">
<head>
<meta charset="utf-8">
<title>Brindlecraft &amp; Quillmarsh Business Card</title>
<link href="https://fonts.googleapis.com/css2?family=Marcellus&family=Lato:wght@300;400&display=swap" rel="stylesheet">
<style>
  :root {
    --navy: #152842;
    --teal: #98aeb9;
    --quill-gray: #4b4c4e;
    --quill-text: #f2f2f2;
    --card-white: #ffffff;
    --ink: #1c1c1c;
    --rule: #d6d9db;
    --mark: #6e8a78;
    --page: #e9eef0;
  }
  * { box-sizing: border-box; margin: 0; padding: 0; }
  html, body {
    width: 1200px; height: 900px; overflow: hidden;
    background: var(--page);
  }
  .sheet { position: relative; width: 1200px; height: 900px; }
  .card {
    position: absolute; left: 250px; width: 700px; height: 400px;
    overflow: hidden;
    box-shadow: 0 2px 8px rgba(0,0,0,0.12);
  }
  .card--quillmarsh { top: 40px; background: var(--quill-gray); color: var(--quill-text); }
  .card--brindlecraft { top: 460px; background: var(--card-white); }

  /* Quillmarsh side */
  .quill-lockup { position: absolute; left: 120px; top: 128px; }
  .quill-name {
    font-family: "Marcellus", serif; font-size: 78px; letter-spacing: 1px;
    line-height: 1; font-weight: 400;
  }
  .quill-byline {
    font-family: "Marcellus", serif; font-size: 15px; letter-spacing: 1px;
    text-align: right; margin-top: 4px;
  }
  .quill-tagline {
    position: absolute; left: 175px; top: 272px;
    font-family: "Lato", sans-serif; font-weight: 300; font-size: 24px; letter-spacing: 0.5px;
  }

  /* Brindlecraft side */
  .brand-lockup {
    position: absolute; right: 46px; top: 48px;
    display: flex; align-items: center; gap: 16px;
  }
  .brand-dot { width: 44px; height: 44px; border-radius: 50%; background: var(--mark); }
  .brand-name {
    font-family: "Marcellus", serif; font-size: 44px; letter-spacing: 1px; color: var(--ink);
  }
  .divider {
    position: absolute; left: 48px; right: 48px; top: 150px;
    height: 1px; background: var(--rule);
  }
  .person { position: absolute; left: 48px; top: 188px; font-family: "Marcellus", serif; }
  .person-name { font-size: 26px; color: var(--navy); letter-spacing: 0.5px; }
  .person-title { font-size: 17px; color: var(--teal); margin-top: 2px; }
  .contact-list { list-style: none; margin-top: 20px; }
  .contact-list li {
    display: flex; align-items: center; gap: 10px;
    font-size: 17px; color: var(--ink); line-height: 26px;
  }
  .contact-list svg { width: 15px; height: 15px; fill: var(--teal); flex: none; }
  .address {
    position: absolute; right: 48px; top: 200px; text-align: right;
    font-family: "Marcellus", serif; font-size: 18px; line-height: 28px; color: var(--ink);
  }
  .edge-band { position: absolute; left: 0; right: 0; bottom: 0; height: 10px; display: flex; }
  .edge-band__navy { width: 58%; background: var(--navy); }
  .edge-band__teal { flex: 1; background: var(--teal); }
</style>
</head>
<body>
<main class="sheet">
  <section class="card card--quillmarsh" aria-label="Quillmarsh side">
    <div class="quill-lockup">
      <div class="quill-name">QUILLMARSH</div>
      <div class="quill-byline">by BRINDLECRAFT</div>
    </div>
    <p class="quill-tagline">Discover the luxury of home.</p>
  </section>

  <section class="card card--brindlecraft" aria-label="Brindlecraft side">
    <div class="brand-lockup">
      <span class="brand-dot"></span>
      <span class="brand-name">BRINDLECRAFT</span>
    </div>
    <div class="divider"></div>

    <div class="person">
      <p class="person-name">DANA WHITLOW</p>
      <p class="person-title">Graphics / Photography Director</p>
      <ul class="contact-list">
        <li>
          <svg viewBox="0 0 16 16" aria-hidden="true"><path d="M3.2 1.5l2.4-.4 1.3 3.1-1.6 1.2c.8 1.7 2.1 3 3.8 3.8l1.2-1.6 3.1 1.3-.4 2.4c-.2.9-1 1.4-1.9 1.3C5.9 12.2 2.3 8.6 1.9 3.4c-.1-.9.4-1.7 1.3-1.9z"/></svg>
          555.201.4870
        </li>
        <li>
          <svg viewBox="0 0 16 16" aria-hidden="true"><path d="M4 1h8v4H4zM2 6h12a1 1 0 011 1v5h-3v3H4v-3H1V7a1 1 0 011-1zm3 6v2h6v-2z"/></svg>
          555.201.4872
        </li>
        <li>
          <svg viewBox="0 0 16 16" aria-hidden="true"><path d="M1 3h14v10H1zm1.5 1.2L8 8.6l5.5-4.4z"/></svg>
          dwhitlow@brindlecraft.com
        </li>
        <li>
          <svg viewBox="0 0 16 16" aria-hidden="true"><path d="M6.5 9.5l3-3 1 1-3 3zM4 8.5l2-2 1 1-2 2a1.4 1.4 0 002 2l2-2 1 1-2 2a2.8 2.8 0 01-4-4zm8-1l-2 2-1-1 2-2a1.4 1.4 0 00-2-2l-2 2-1-1 2-2a2.8 2.8 0 014 4z"/></svg>
          www.brindlecraft.com
        </li>
      </ul>
    </div>

    <address class="address" style="font-style:normal">
      PO Box 417<br>
      1840 Larkspur Ridge Rd.<br>
      Fernbrook, VA 20417
    </address>

    <div class="edge-band">
      <span class="edge-band__navy"></span>
      <span class="edge-band__teal"></span>
    </div>
  </section>
</main>
</body>
</html>
```